Super urgent - business card design

I need to design a business card
on the front side the words "VORIAN PARTNERS" with the top half surrounded by a stylised cloud. Minimalist, navy blue font on white background, with the Vorian partners in embossing.

On the back contact details (avoid centered). I would rather have the details taking the 2/3rd on the right and having the logo on the left, but anyway not plain centered

Marcello Tavoletti
CEO e Fondatore

m.tavoletti@vorian-partners.example
+39.331.584.2064

Piazza Lunetti 7
20145 Milano

```html
<!DOCTYPE html>
<html lang="it">
<head>
<meta charset="utf-8">
<title>Vorian Partners – Biglietto da visita</title>
<link href="https://fonts.googleapis.com/css2?family=Jost:wght@400;500&display=swap" rel="stylesheet">
<style>
  :root {
    --backdrop: #232c33;
    --navy: #020f3a;
    --paper: #ffffff;
    --ink-light: #ffffff;
  }
  html, body {
    margin: 0;
    padding: 0;
    width: 1158px;
    height: 1200px;
    overflow: hidden;
    background: var(--backdrop);
    font-family: "Jost", "Futura", sans-serif;
  }
  .stage {
    position: relative;
    width: 1158px;
    height: 1200px;
  }
  .card {
    position: absolute;
    top: 104px;
    width: 467px;
    height: 268px;
    box-shadow: 0 14px 18px -12px rgba(0,0,0,0.55);
  }
  .card--front {
    left: 97px;
    background: var(--paper);
    color: var(--navy);
  }
  .card--back {
    left: 594px;
    background: var(--navy);
    color: var(--ink-light);
  }
  .wordmark {
    position: absolute;
    text-align: center;
    font-weight: 500;
    text-transform: uppercase;
    line-height: 1.25;
    white-space: nowrap;
  }
  .wordmark__line { display: block; }
  .card--front .wordmark {
    left: 0; right: 0;
    top: 106px;
    font-size: 30px;
    letter-spacing: 0.16em;
  }
  .card--back .wordmark {
    left: 30px;
    width: 160px;
    top: 112px;
    font-size: 21px;
    letter-spacing: 0.14em;
  }
  .contact {
    position: absolute;
    left: 207px;
    top: 61px;
    font-weight: 400;
    line-height: 1.25;
  }
  .contact__name {
    margin: 0;
    font-size: 18px;
    font-weight: 400;
  }
  .contact__role {
    margin: 0 0 22px;
    font-size: 11px;
    letter-spacing: 0.08em;
    text-transform: uppercase;
  }
  .contact__block {
    margin: 0 0 18px;
    font-size: 14px;
    letter-spacing: 0.02em;
    line-height: 1.3;
  }
</style>
</head>
<body>
<main class="stage">
  <section class="card card--front" aria-label="Fronte del biglietto">
    <div class="wordmark">
      <span class="wordmark__line">Vorian</span>
      <span class="wordmark__line">Partners</span>
    </div>
  </section>

  <section class="card card--back" aria-label="Retro del biglietto">
    <div class="wordmark">
      <span class="wordmark__line">Vorian</span>
      <span class="wordmark__line">Partners</span>
    </div>
    <div class="contact">
      <h1 class="contact__name">Marcello Tavoletti</h1>
      <p class="contact__role">CEO e Fondatore</p>
      <p class="contact__block">m.tavoletti@vorian-partners.example<br>+39.331.584.2064</p>
      <p class="contact__block">Piazza Lunetti 7<br>20145 Milano</p>
    </div>
  </section>
</main>
</body>
</html>
```